Major Australian Food and Wine Event Web Design Project

The project will consist of 3 designs
The homepage
A city hub page
A general content page

The main audience who will visit the website will be (in Order of importance:

1) Visitors
- Mainly women 24 – 54 years (they are the main ticket buyers)
- In a relationship – so will go to the show with their partner
- In a good paying job or home maker – and who have disposable income to spend $30 a ticker
- Enjoy food, wine and going out
- Looking for a fun day out – although an event that is about food and wine – it is an event that most people will go to and have a fun day out – not too pretentious

A smaller proportion of the audience will be:
2) Exhibitors & sponsors ( both prospective and existing)
3) Media

Objectives:

- Functionality on home page and sub pages needs to be updated, clear, easy to navigate and inject a sense of ‘fun’ – need to make it look more professional
- Need to incorporate the many things that need to be on the home page and sub pages in a visually appealing manner
- Ensure the ‘Cons’ above are considered and reflected in functionality and design
- To not be too focus on the colours (these can be changed) – but focus on the functionality and overall design opportunities.

Approach:

Keywords to describe the Bright Plate & Vine Fair:
Fun day out, discover, learn, indulge, entertaining

Other website examples:

Some great consumers event websites from the UK really make our website look basic and juvenile – and below are some examples of the presentation of how we would like our website to look like:

http://www.morselfairs-example.com/london/ This website is clean, includes good social media integration and exudes a sense of fun. Their content pages, such as the features landing page also presents options in a clear and visually appealing way with a series of boxes including image and text http://www.morselfairs-example.com/london/content/343/Features

http://www.homecraftexpo-example.com/ - this is also a great website – and it incorporates all the elements we would be looking for on our homepage – but the background/skin also includes a sense of fun and cheekiness. Subpages also are consistent.

Features

• Its a fun day that offers great value for money
• Caters to all visitors, regardless of different levels of knowledge or interest in food, wine and cooking.
• Sample great quality food and wine products from hundreds of reputable exhibitors
• Learn more through many of the shows feature activities (Celeb Theatre, Wine Theatre, Cooking & Cheese Classes)

Functionality & Structure:

In a user friendly, easy to view way, we need to incorporate the following functionality elements on home page:
- main header (that will incorporate our current creative) with a ‘fun’ skin
- navigation tabs/references (hone, location, tickets, blog, sign up, exhibitors)
- navigation/content banner (rotating)
- Area for small intro about the show
- News and highlight section
- New exhibitors section
- Obvious Ticket call to action
- Obvious sign up call to action
- Social media buttons or links ( really like the moving gifs on the Homecraftexpo-example.com site
- area for advertising (MREC size) to sell to exhibitors/sponsors
- Show dates for all 5 shows (maybe in main header)

Subpage layout is also important and needs to reflect the homepage – so would also like to see examples of how this would look and tie in with navigation – we generally have a lot of content on these pages, so clear navigation would be useful. – see below for further details of functionality for city Hubs

‘CITY HUB’ BRIEF
When navigating to each location the user will be taken to a ‘CITY HUB’ which should replicate design and content elements of a main HOME page, as well as reflect more specific information for each Show. Elements which must appear on this page are:
• FEATURES – which may be displayed in categories (in boxes, see appendix 1.0) which will link through to relevant content pages. Or in one box which will link through to a features page with all presented in boxes
• CHEFS – may be displayed as a separate icon box which will link to chefs page with bios, Celeb Theatre timetable etc.
• TICKETS – either a button or clear callout to purchase tickets
• PLAN YOUR DAY – may be displayed in a separate content box which will then link through to getting there, sample itineraries and downloadable pocket show guide for visitors to print before coming to the Show.
• WHO’S EXHIBITING – to link back to city specific exhibitor lists

Our current website is out of date and has the following inadequacies (www.brightplatefair-example.com.au) -

The homepage
A city hub page
A general content page

1) Visitors

3) Media

Objectives:

Approach:

To be perceived as a fun, entertaining event with something for everyone - website creative and navigation must reflect this.

Other website examples:

Features

- New exhibitors section

‘CITY HUB’ BRIEF

- Dated design/layout
- Homepage too text heavy
- No content boxes that can be used for different features/areas (eg. News, Exhibitors etc)
- Uninspiring colours and skin(eg. grey background), does not reflect ‘a fun day out’
- Limited presence of social media platforms and lacks ‘community’
- No continuity in sub pages
- main banner too big – takes up too much space on homepage

Requirements
Must have
• As per above brief.

In addition:
Floating social media buttons on side
Wrap around image
Drop down menu (specifically for the location nav item)

```html
<!DOCTYPE html>
<html lang="en">
<head>
<meta charset="utf-8">
<title>Bright Plate &amp; Vine Fair</title>
<link rel="stylesheet" href="https://fonts.googleapis.com/css2?family=Arvo:wght@400;700&family=Cabin:wght@400;500;600&display=swap">
<style>
:root{
  --red:#d61f1f;
  --red-dark:#a90f0f;
  --orange:#f39a1e;
  --orange-light:#fbc46a;
  --cream:#f8c978;
  --ink:#222;
  --muted:#555;
  --footer:#262626;
  --panel:#f4f4f4;
  --line:#d8d8d8;
  --white:#fff;
}
*{box-sizing:border-box;margin:0;padding:0}
html,body{width:1078px;height:1200px;overflow:hidden}
body{position:relative;font-family:"Cabin",Arial,sans-serif;color:var(--ink);background:#fff}
.abs{position:absolute}
.skin{left:0;top:0;width:1078px;height:1046px;
  background:radial-gradient(ellipse at 10% 20%,#b52c2c 0,#d9776a 25%,transparent 55%),
  radial-gradient(ellipse at 92% 15%,#b82a2a 0,#e08a70 25%,transparent 55%),
  radial-gradient(ellipse at 95% 55%,#c23d3a 0,#e7a590 20%,transparent 45%),
  linear-gradient(180deg,#e8b59a 0,#f3dccd 55%,#fff 85%)}
.page{left:208px;top:0;width:662px;height:1046px;background:var(--white)}
.logo-box{left:229px;top:0;width:135px;height:104px;background:#f3f3f3;border:1px solid #ddd;border-top:0;border-radius:0 0 6px 6px;box-shadow:0 3px 6px rgba(0,0,0,.15);display:flex;align-items:center;justify-content:center;text-align:center;padding:8px;font:600 19px/1.1 "Cabin",sans-serif;color:var(--ink)}
.util{left:620px;top:42px;width:228px;height:28px;background:#e8f3fb;border:1px solid #bcd8ec;border-radius:5px;display:flex;align-items:center;justify-content:center;font:8px Arial,sans-serif;color:#1d3b5e}
.util span{padding:0 7px;border-left:1px solid #9bbbd6}
.util span:first-child{border-left:0}
.nav{left:226px;top:113px;width:627px;height:33px;background:linear-gradient(#e22424,#c41515);border-radius:5px;box-shadow:0 2px 3px rgba(0,0,0,.25)}
.nav a{position:absolute;top:12px;font:600 9px Arial,sans-serif;color:#fff;text-decoration:none}
.nav a.current{color:#ffe34a;text-decoration:underline}
.search{left:479px;top:9px;width:135px;height:17px;background:#fdf0ee;border-radius:9px;font:italic 7px Arial,sans-serif;color:#555;padding:5px 9px}
.search i{position:absolute;right:0;top:0;width:20px;height:17px;background:#333;border-radius:0 9px 9px 0}
.banner{left:224px;top:161px;width:630px;height:224px;border:2px solid #ccc;border-radius:6px;overflow:hidden;
  background:linear-gradient(90deg,#6a4a2a 0,#c79a5e 25%,#e9c79a 45%,#b98b55 70%,#7a5a3a 100%)}
.banner-caption{left:0;top:141px;width:408px;height:75px;background:rgba(40,30,20,.6)}
.banner-caption h2{position:absolute;left:23px;top:12px;font:400 20px "Arvo",serif;color:#fff;letter-spacing:.5px}
.banner-caption p{position:absolute;left:23px;top:39px;font:400 10.5px/1.3 "Arvo",serif;color:#fff;width:230px}
.dots{left:240px;top:209px;display:flex;gap:6px;align-items:center}
.dots b{width:8px;height:8px;border-radius:50%;background:#fff}
.dots .arr{width:13px;height:13px;background:#111;border:1px solid #fff}
.updates{left:632px;top:192px;width:204px;height:166px;background:var(--cream);border:1px solid #e9a94a;border-radius:3px;opacity:.97}
.updates h3{font:400 15px "Arvo",serif;text-align:center;margin:8px 0 4px;color:#222}
.updates table{width:100%;border-collapse:collapse;font:400 11.5px "Cabin",sans-serif}
.updates td{padding:5px 5px;border-top:1px dotted #a77a2a;height:26px}
.float-social{left:870px;top:210px;width:32px;height:132px;background:#fff;border-radius:0 5px 5px 0;box-shadow:1px 1px 4px rgba(0,0,0,.25)}
.float-social i{position:absolute;left:4px;width:23px;height:23px;background:#8a8a8a;border-radius:3px}
.book-tab{left:174px;top:422px;width:34px;height:132px;background:#fff;border-radius:5px 0 0 5px;box-shadow:-2px 1px 4px rgba(0,0,0,.2)}
.book-tab span{position:absolute;left:-44px;top:55px;width:122px;transform:rotate(-90deg);font:500 15px "Cabin",sans-serif;color:var(--red);text-align:center}
.intro{left:223px;top:420px;width:415px}
.intro h1{font:400 18px "Cabin",sans-serif;color:#333;letter-spacing:-.3px}
.intro h1 em{font-style:normal;color:var(--red)}
.intro .lead{font-size:10px;color:#555;margin:4px 0 12px}
.intro p{font-size:8.6px;line-height:1.25;margin-bottom:10px;color:#222}
.signup-band{left:198px;top:576px;width:293px;height:27px;background:linear-gradient(var(--orange-light),var(--orange));clip-path:polygon(0 0,100% 0,98% 100%,0 100%);font:10px "Cabin",sans-serif;color:#fff;padding:7px 23px}
.cta{left:670px;width:210px;height:30px;background:linear-gradient(#fff,#ececec);border:1px solid #bbb;border-right:0;border-radius:6px 0 0 6px;font:500 14px "Cabin",sans-serif;color:var(--red);padding:6px 0 0 42px;letter-spacing:-.4px;box-shadow:0 2px 2px rgba(0,0,0,.12)}
.cta::after{content:"";position:absolute;right:-1px;bottom:-8px;border-left:9px solid transparent;border-top:8px solid #222}
.cta .ico{position:absolute;left:14px;top:6px;width:18px;height:18px}
.tab{top:630px;height:19px;border-radius:4px 4px 0 0;font:10px "Arvo",serif;color:#fff;text-align:center;padding-top:4px}
.gallery{left:227px;top:649px;width:409px;height:211px;background:#fafafa;border:1px solid var(--line);border-radius:3px}
.thumb{position:absolute;width:83px;height:52px;box-shadow:0 1px 2px rgba(0,0,0,.3)}
.side-head{left:657px;height:19px;background:linear-gradient(var(--orange-light),var(--orange));border-radius:5px 5px 0 0;font:500 9px "Cabin",sans-serif;color:#fff;padding:4px 5px}
.side-panel{left:648px;top:649px;width:214px;height:299px;background:var(--panel);border:1px solid var(--line);border-radius:3px}
.books{left:660px;top:658px;width:178px;height:54px;background:linear-gradient(90deg,#777,#ddd 35%,#9a7a5a 60%,#eee)}
.shop-text{left:660px;top:724px;width:190px;font:6.6px/1.6 Arial,sans-serif;color:#333}
.shop-text a{color:var(--red);text-decoration:none}
.tile{position:absolute;width:91px;height:51px;background:var(--red);border:1px solid #fff;box-shadow:0 0 0 1px #c33;color:#fff;text-align:center}
.tile b{display:block;font:600 9px "Cabin",sans-serif;margin-top:14px}
.tile small{position:absolute;left:0;right:0;bottom:3px;font:5px Arial,sans-serif}
.social-h{left:223px;top:879px;font:400 14px "Cabin",sans-serif;color:var(--red)}
.social-p{left:223px;top:902px;width:340px;font:6.5px/1.4 Arial,sans-serif;color:#222}
.nets{top:945px;font:600 13px "Cabin",sans-serif;color:#2c4a8a}
.bird{left:219px;top:968px;width:40px;height:44px;border-radius:50%;background:radial-gradient(#9fd6f2,#4aa8d8 60%,transparent 62%)}
.tweet{left:267px;top:975px;width:207px;height:31px;background:#ececec;border-radius:3px;padding:4px 5px;font:9px "Cabin",sans-serif}
.tweet small{display:block;font:7px Arial,sans-serif}
.tweet small a,.twlink{color:#2a7ac0;text-decoration:none}
.twlink{left:271px;top:1011px;font:7px Arial,sans-serif}
.updates-band{left:588px;top:958px;width:292px;height:30px;background:linear-gradient(var(--orange-light),var(--orange));padding:4px 11px;color:#222}
.updates-band b{display:block;font:500 9.5px/1.2 "Cabin",sans-serif}
.updates-band span{display:block;font:6.5px/1.2 Arial,sans-serif}
.updates-band::after{content:"";position:absolute;right:0;bottom:-7px;border-left:8px solid transparent;border-top:7px solid #222}
.sponsor{top:1010px;font:600 10px "Cabin",sans-serif;color:#222}
.wine-photo{left:40px;top:868px;width:168px;height:332px;border-radius:6px;
  background:radial-gradient(ellipse at 50% 60%,#3a2626 0,#2a1d1d 45%,rgba(42,29,29,.35) 75%,rgba(42,29,29,0) 100%)}
.footer{left:0;top:1046px;width:1078px;height:154px;background:var(--footer)}
.fcol{top:1065px;font:7.6px/1.28 Arial,sans-serif;color:#fff}
.fcol h4{font:700 8px Arial,sans-serif;margin-bottom:11px}
.org-mark{left:693px;top:1061px;width:91px;height:24px;background:var(--red);font:600 11px "Cabin",sans-serif;color:#fff;padding:5px 7px}
.org{left:693px;top:1118px;font:7px/1.4 Arial,sans-serif;color:#fff}
</style>
</head>
<body>
<div class="abs skin" role="img" aria-label="Soft focus close-up of colourful food wrapping around the page"></div>
<div class="abs page"></div>

<header>
  <div class="abs logo-box">Bright Plate &amp; Vine Fair</div>
  <nav class="abs util"><span>Contact Us</span><span>News &amp; Media Releases</span><span>Sponsors</span></nav>
  <nav class="abs nav">
    <a class="current" style="left:22px" href="#">Home</a>
    <a style="left:90px" href="#">Location</a>
    <a style="left:170px" href="#">Tickets</a>
    <a style="left:242px" href="#">Blog</a>
    <a style="left:310px" href="#">Sign up</a>
    <a style="left:387px" href="#">Exhibitors</a>
    <div class="abs search">search...<i></i></div>
  </nav>
</header>

<section class="abs banner">
  <div class="abs" role="img" aria-label="Smiling chef in a white hat in a busy commercial kitchen" style="left:0;top:0;width:630px;height:224px"></div>
  <div class="abs banner-caption">
    <h2>SUCCUMB TO YOUR SENSES</h2>
    <p>BE INSPIRED BY OUR CELEBRITY CHEFS LIVE ON STAGE</p>
  </div>
  <div class="abs dots"><b class="arr"></b><b></b><b></b><b></b><b></b><b></b><b></b><b></b><b></b><b class="arr"></b></div>
</section>

<aside class="abs updates">
  <h3>LATEST UPDATES</h3>
  <table>
    <tr><td>Melbourne</td><td>June 1 -3, 2012</td></tr>
    <tr><td>Sydney</td><td>June 22 -24, 2012</td></tr>
    <tr><td>Perth</td><td>July 13 - 15, 2012</td></tr>
    <tr><td>Adelaide</td><td>October 12 - 14, 2012</td></tr>
    <tr><td>Brisbane</td><td>November 9 - 11, 2012</td></tr>
  </table>
</aside>

<div class="abs float-social" aria-label="Social links">
  <i style="top:11px"></i><i style="top:40px"></i><i style="top:69px"></i><i style="top:98px"></i>
</div>

<div class="abs book-tab"><span>BOOK TICKETS</span></div>

<section class="abs intro">
  <h1><em>The Bright Plate &amp; Vine Fair</em> all over for another year!</h1>
  <p class="lead">What a year for good food and wine!</p>
  <p>Melbourne, Sydney, Perth, Adelaide and Brisbane have all had the chance to experience the fun, excitement and joy, that is the Bright Plate &amp; Vine Fair!</p>
  <p>We would like to thank all our amazing visitors for coming along and helping us celebrate another awesome year - A big thank you also to the rest of the crew including exhibitors, sponsors and chefs!</p>
  <p>Make sure you visit the website early next year for all the details of the 2012 Shows - or sign up to our newsletter to be the first to find out when we are on sale and to receive special discounts and offers!</p>
</section>
<div class="abs signup-band">Sign up to the Bright Plate &amp; Vine Fair e-newsletter</div>

<div class="abs cta" style="top:427px"><svg class="ico" viewBox="0 0 18 18"><rect x="2" y="5" width="14" height="9" rx="1" fill="#f3b81e" transform="rotate(-20 9 9)"/></svg>Get tickets</div>
<div class="abs cta" style="top:464px"><svg class="ico" viewBox="0 0 18 18"><rect x="2" y="5" width="14" height="11" rx="1" fill="#7cb342"/><rect x="5" y="2" width="8" height="4" fill="#555"/></svg>Wants to exhibit?</div>
<div class="abs cta" style="top:502px"><svg class="ico" viewBox="0 0 18 18"><circle cx="9" cy="9" r="8" fill="#3b5b9a"/></svg>Like us on Chatterbook</div>
<div class="abs cta" style="top:539px"><svg class="ico" viewBox="0 0 18 18"><circle cx="9" cy="5" r="3.5" fill="#444"/><path d="M3 17c0-5 3-8 6-8s6 3 6 8z" fill="#444"/></svg>Volunteer for the show</div>
<div class="abs cta" style="top:577px"><svg class="ico" viewBox="0 0 18 18"><rect x="1" y="3" width="16" height="14" rx="1" fill="#fff" stroke="#666"/><rect x="1" y="3" width="16" height="4" fill="#6ab04c"/><text x="9" y="15" font-size="7" text-anchor="middle" font-family="Arial" font-weight="700">26</text></svg>Keep up to date</div>

<div class="abs tab" style="left:236px;width:58px;background:var(--red)">News</div>
<div class="abs tab" style="left:294px;width:83px;background:var(--orange)">Highlights</div>
<section class="abs gallery">
  <div class="thumb" role="img" aria-label="Audience at a stage presentation" style="left:12px;top:13px;background:linear-gradient(#1b2350,#6a2a4a)"></div>
  <div class="thumb" role="img" aria-label="Exhibition hall entrance" style="left:111px;top:13px;background:linear-gradient(#2a2a2a,#c9c2a8)"></div>
  <div class="thumb" role="img" aria-label="Chef speaking on stage" style="left:210px;top:13px;background:linear-gradient(90deg,#d8c09a,#f2f0ea)"></div>
  <div class="thumb" role="img" aria-label="Chef chatting with a visitor" style="left:309px;top:13px;background:linear-gradient(90deg,#e8e2d8,#6a4a30)"></div>
  <div class="thumb" role="img" aria-label="Visitor at an exhibitor stand" style="left:12px;top:81px;background:linear-gradient(90deg,#a0846a,#4a7ab0)"></div>
  <div class="thumb" role="img" aria-label="Crowd around a demonstration" style="left:111px;top:81px;background:linear-gradient(#1f2a4a,#5a5a6a)"></div>
  <div class="thumb" role="img" aria-label="Colourful cupcakes" style="left:210px;top:81px;background:linear-gradient(90deg,#e8a0b0,#f4d07a,#8ab0d8)"></div>
  <div class="thumb" role="img" aria-label="Rows of red exhibitor stands" style="left:309px;top:81px;background:linear-gradient(#d8d0c8,#a03030)"></div>
  <div class="thumb" role="img" aria-label="Decorated cupcake close-up" style="left:12px;top:148px;background:linear-gradient(#9ec8a0,#e8f0e0)"></div>
  <div class="thumb" role="img" aria-label="Plated dish of food" style="left:111px;top:148px;background:linear-gradient(#6a3a1a,#d09050)"></div>
  <div class="thumb" role="img" aria-label="Busy exhibition floor from above" style="left:210px;top:148px;background:linear-gradient(#c8c8d0,#3a3a4a)"></div>
  <div class="thumb" role="img" aria-label="Visitors sampling food" style="left:309px;top:148px;background:linear-gradient(#5a4a3a,#2a2a2a)"></div>
</section>

<div class="abs side-head" style="top:630px;width:193px">Bright Plate &amp; Vine Fair Online Book Shop</div>
<div class="abs side-panel"></div>
<div class="abs books" role="img" aria-label="Row of celebrity chef cookbook covers"></div>
<p class="abs shop-text">Here you will be able to get some fantastic discounts on a huge range of top quality cook books, including titles from Graham Rowley, Ben Garside, Dana Holt and many more, all well below the usual retail price.<br>Check out <a href="#">what's in stock.</a></p>
<div class="abs side-head" style="top:797px;width:193px">Exhibitors &amp; Sponsors</div>
<div class="abs" style="left:666px;top:828px">
  <div class="tile" style="left:0;top:0"><b>Fine Table Expo</b><small>www.finetableexpo-example.com.au</small></div>
  <div class="tile" style="left:93px;top:0"><b>kitchenworks</b><small>www.kitchenworks-example.com</small></div>
  <div class="tile" style="left:0;top:53px"><b>Wholegrain Free Fair</b><small>www.wholegrainfree-example.com.au</small></div>
  <div class="tile" style="left:93px;top:53px"><b>Homecraft Expo Live</b><small>www.homecraftexpo-example.com.au</small></div>
</div>

<h2 class="abs social-h">The Bright Plate &amp; Vine Fair Social Networks</h2>
<p class="abs social-p">Lorem Ipsum is simply dummy text of the printing and typesetting industry. industry's standard dummy text ever since the 1500s, when an unknown printer took a galley of type and scrambled it to make a type specimen book. It has survived not only five centuries.</p>
<span class="abs nets" style="left:274px">Chatterbook</span>
<span class="abs nets" style="left:362px">Pixshare</span>
<span class="abs nets" style="left:424px">Vidcast</span>
<div class="abs bird" role="img" aria-label="Cartoon bird reading a book"></div>
<div class="abs tweet">Catering Tweets<small>Estrenando donimio @ <a href="#">hostbox 338 days ago</a></small></div>
<a class="abs twlink" href="#">Sign in to Chirpline</a>

<div class="abs updates-band"><b>Receive show updates</b><span>get updated on chef line-ups, ticket sale dates and show times</span></div>
<span class="abs sponsor" style="left:606px;background:#111;color:#fff;padding:2px 5px">Harrow &amp; Pell</span>
<span class="abs sponsor" style="left:707px">Glassmere</span>
<span class="abs sponsor" style="left:790px;font-size:8px">Ridgeford Estates</span>

<div class="abs wine-photo" role="img" aria-label="Photograph of three bottles of red wine with illustrated labels"></div>

<footer>
  <div class="abs footer"></div>
  <div class="abs fcol" style="left:237px"><h4>Bright Plate &amp; Vine Fair</h4>Home<br>Melbourne<br>Sydney<br>Perth<br>Adelaide<br>Brisbane<br>Want to Exhibit?<br>Recipe Club</div>
  <div class="abs fcol" style="left:405px"><h4>Show Attractions</h4>Celebrity Theatre<br>Cheese Masterclass<br>Cooking School<br>Decanter Bar<br>Restaurant<br>Wine Theatre<br>Exhibitor list<br>Floor plans</div>
  <div class="abs fcol" style="left:570px"><h4>Chef Bio's</h4>Alana Grey<br>Garth Menzies<br>Greg Callister<br>Marc Fenwick<br>Mitch Morrow<br>Toby Pickard<br><h4 style="margin:17px 0 13px">Recipe Club</h4>Login</div>
  <div class="abs org-mark">meridian</div>
  <p class="abs org">Event organised by<br><b>Meridian Events Australia.© 2007.</b><br><br><br>Competition Terms &amp; Conditions</p>
</footer>
</body>
</html>
```